Relaunch website https://dancepastdawn.de/

We are looking for creative minds to relaunch the website for our new musical “Dance past dawn” (www.dancepastdawn.de). The aim is to convey the full emotional power, spine-tingling intensity, and spirit of empowerment of this unique production.

The site should make the emotional depth and power of the musical come to life - not merely by describing it, but by letting people feel it. In accordance with our marketing philosophy: "Show, don't tell"—we tell the story, rather than simply promoting the musical.

The website should be responsive, offer intuitive navigation and be in accordance with the design guidelines. Please design the website with the compatibility of a specific WordPress theme in mind (in the best case choose from a big enterprise theme such as avada, enfold or divi).

Design specifications:
Primary color: Pink (R224 / G51 / B151)
Secondary color: yellow (R255 / G221 / B0)
Tertiary color: black (R29 / G29 / B27)
Font-Headline: Tungsten
Font body: DIN 1451 LT Pro
Background texture: Grunge

In addition to the main page, the following subpages will be relevant:
OURtale, The Musical, Cast & Team, Tickets, Plan your visit, Corporate events, Press, FAQ, Coupon, News

The winner will be selected according to the following criteria: creativity, user guidance, technical feasibility and compliance with the style guide. Also based on your unique ideas! We know the briefing is super specific but please let your ideas and feedback flow.

We have uploaded a detailed briefing document (including the CI) in German and English as well as the logos. You can use all available graphics from the current website and socials if needed for your pitch. Please design at least the following pages:
- Home (briefing included)
- OURTale (be creative - no specific briefing)
- Ticketing (separate briefing included)
- Corporate events (separate briefing included)
- Plan your visit (separate briefing included)
- News (be creative - no specific briefing)

If you have any questions, please contact marla.fenwick@dosuvel-entertainment.

We would love to give you more time for your designs!

Target Market(s)

Germany

Industry/Entity Type

Musical & Entertainment

Number of Pages Required

5+ page

Font styles to use
Other font styles liked:
• Headline: Tungsten & Body: DIN 1451 LT Pro

Colors
FFF300
FFF600
FEFA6F
FFFEC7
FFFEE8
E54698
E96AAD
F1A4CE
F9D9EA
FCEFF6

Requirements
Must have
• See briefing
Nice to have
• See briefing
Should not have
• See briefing

```html
<!DOCTYPE html>
<html lang="de">
<head>
<meta charset="utf-8">
<title>Dance past dawn – Das Musical</title>
<link rel="stylesheet" href="https://fonts.googleapis.com/css2?family=League+Gothic&family=Barlow:wght@400;500;600&family=Barlow+Condensed:wght@500;600&display=swap">
<style>
:root{
  --pink:#e03397;
  --yellow:#ffdd00;
  --black:#1d1d1b;
  --ink:#0e0e0d;
  --white:#f2f0ec;
  --grey:#b9b6b0;
  --head:"League Gothic",sans-serif;
  --cond:"Barlow Condensed",sans-serif;
  --body:"Barlow",sans-serif;
}
*{box-sizing:border-box;margin:0;padding:0}
html,body{width:1200px;height:2720px;overflow:hidden;background:var(--ink);color:var(--white);font-family:var(--body)}
.page{position:relative;width:1200px;height:2720px;overflow:hidden}
section,header,footer{position:absolute;left:0;width:1200px}
a{color:inherit;text-decoration:none}
.btn{position:absolute;display:flex;align-items:center;justify-content:center;gap:12px;font-family:var(--cond);font-weight:600;font-size:18px;letter-spacing:.5px;text-transform:uppercase}
.btn-pink{background:var(--pink);color:#fff}
.btn-outline{border:2px solid #fff;color:#fff}
.arrow{width:24px;height:12px}

/* header */
.site-header{top:0;height:100px;z-index:5}
.brand-kicker{position:absolute;left:36px;top:26px;font-family:var(--cond);font-weight:600;font-size:13px;letter-spacing:.5px}
.brand{position:absolute;left:34px;top:36px;font-family:var(--head);font-size:64px;line-height:1;color:var(--yellow);letter-spacing:.5px}
.brand-sub{position:absolute;left:282px;top:99px;font-family:var(--cond);font-size:10px;letter-spacing:4px}
.nav{position:absolute;left:451px;top:62px;display:flex;gap:26px;font-family:var(--cond);font-weight:600;font-size:13px;text-transform:uppercase}
.nav-cta{left:1038px;top:54px;width:146px;height:34px;font-size:13px}

/* hero */
.hero{top:0;height:800px;background:radial-gradient(ellipse at 65% 25%,#4a3a33 0%,#1a1614 55%,#0e0e0d 80%)}
.hero-photo{position:absolute;left:440px;top:120px;width:760px;height:680px;background:radial-gradient(ellipse at 55% 45%,#8d7e72 0%,#4b3f38 40%,#1d1917 75%,transparent 100%)}
.hero-splash{position:absolute;right:0;bottom:0;width:420px;height:260px;background:radial-gradient(ellipse at 80% 80%,rgba(224,51,151,.75),transparent 65%)}
.hero-title{position:absolute;left:54px;top:186px;font-family:var(--head);font-size:98px;line-height:.82;text-transform:uppercase}
.hero-title .pink{color:var(--pink)}
.hero-title .yellow{color:var(--yellow)}
.hero-lead{position:absolute;left:57px;top:605px;font-size:18px;line-height:1.55}
.hero .btn-pink{left:57px;top:695px;width:194px;height:54px}
.hero .btn-outline{left:306px;top:695px;width:218px;height:54px}
.badge{position:absolute;left:965px;top:545px;width:200px;height:200px;border-radius:50%;background:var(--pink);transform:rotate(-8deg);display:flex;flex-direction:column;align-items:center;justify-content:center;font-family:var(--head);text-transform:uppercase;line-height:.95}
.badge .b1{font-size:30px}
.badge .b2{font-size:48px;color:var(--yellow)}
.badge .b3{font-size:40px}

/* ticker */
.ticker{top:800px;height:70px;background:var(--ink);border-top:2px solid #e7e4de;border-bottom:1px solid #333;display:flex;align-items:center;gap:28px;padding-left:34px;font-family:var(--cond);font-weight:500;font-size:17px;color:var(--pink);white-space:nowrap;text-transform:uppercase}
.star{color:var(--yellow);font-size:18px}

/* story */
.story{top:870px;height:495px;background:linear-gradient(90deg,#111 0%,#141313 35%,#2a1020 100%)}
.story-title{position:absolute;left:58px;top:52px;font-family:var(--head);font-size:70px;line-height:.84;text-transform:uppercase}
.story-title .yellow{color:var(--yellow)}
.story-text{position:absolute;left:59px;top:238px;width:340px;font-size:16px;line-height:1.6}
.story-claim{position:absolute;left:59px;top:348px;font-family:var(--head);font-size:32px;color:var(--pink);letter-spacing:.5px}
.story .btn-outline{left:58px;top:400px;width:226px;height:50px;justify-content:space-between;padding:0 22px;border-width:1px;font-size:15px}
.collage{position:absolute;left:430px;top:22px;width:750px;height:460px;background:radial-gradient(ellipse at 70% 40%,rgba(224,51,151,.45),transparent 70%)}
.clip{position:absolute;border:8px solid #d8d0c0}
.clip-1{left:20px;top:50px;width:300px;height:300px;background:linear-gradient(#6d6a66,#2f2d2b);transform:rotate(-3deg)}
.clip-2{left:270px;top:22px;width:300px;height:240px;background:linear-gradient(#cfc3a9,#9b8f78);border-color:#c6b99e;transform:rotate(-4deg)}
.clip-3{left:140px;top:250px;width:340px;height:200px;background:linear-gradient(#77736e,#3a3835);transform:rotate(-6deg)}
.clip-4{left:440px;top:220px;width:300px;height:230px;background:linear-gradient(#8a8175,#4a443d);transform:rotate(-3deg)}

/* lead character */
.lead{top:1365px;height:445px;background:radial-gradient(ellipse at 85% 60%,rgba(224,51,151,.55),transparent 45%),radial-gradient(ellipse at 10% 100%,rgba(224,51,151,.6),transparent 35%),#121111;border-top:2px solid #e7e4de}
.portrait{position:absolute;left:110px;top:0;width:390px;height:445px;background:radial-gradient(ellipse at 50% 35%,#8a6856 0%,#4a3529 45%,#1b1513 80%,transparent 100%)}
.lead-kicker{position:absolute;left:601px;top:55px;font-family:var(--head);font-size:26px;color:var(--pink);letter-spacing:.5px}
.lead-name{position:absolute;left:598px;top:80px;font-family:var(--head);font-size:132px;line-height:1;text-transform:uppercase}
.lead-text{position:absolute;left:601px;top:225px;width:300px;font-size:17px;line-height:1.55}
.lead .btn-pink{left:601px;top:352px;width:282px;height:50px;font-size:17px}

/* title band */
.band{top:1810px;height:305px;background:radial-gradient(ellipse at 50% 30%,rgba(224,51,151,.55),transparent 60%),#161414;border-top:2px solid #e7e4de}
.band-title{position:absolute;left:0;width:1200px;top:26px;text-align:center;font-family:var(--head);font-size:180px;line-height:1;color:var(--yellow);text-transform:uppercase;letter-spacing:2px}
.band-sub{position:absolute;left:0;width:1200px;top:186px;text-align:center;font-family:var(--head);font-size:36px;letter-spacing:1.5px}
.band .btn-pink{left:463px;top:234px;width:278px;height:48px;font-size:18px}

/* stats */
.stats{top:2115px;height:150px;background:#0b0b0a;border-top:1px solid #2a2a2a;border-bottom:1px solid #2a2a2a;display:flex}
.stat{flex:1;display:flex;align-items:center;gap:30px;padding-left:60px;border-right:2px solid var(--pink);margin:22px 0}
.stat:last-child{border-right:none}
.stat svg{width:82px;height:82px;flex:none}
.stat-num{font-family:var(--head);font-size:50px;line-height:1;color:var(--yellow)}
.stat-label{font-family:var(--head);font-size:26px;letter-spacing:.8px;text-transform:uppercase}

/* press */
.press{top:2265px;height:225px;background:#0e0e0d}
.press-title{position:absolute;left:58px;top:30px;font-family:var(--head);font-size:28px;color:var(--pink);letter-spacing:.8px;text-transform:uppercase}
.quote{position:absolute;top:80px;width:230px}
.quote-mark{position:absolute;left:-34px;top:-4px;font-family:var(--head);font-size:44px;color:var(--pink);line-height:1}
.quote p{font-size:14px;line-height:1.6}
.quote cite{display:block;margin-top:18px;font-family:var(--cond);font-style:normal;font-size:14px;color:var(--pink);text-transform:uppercase}
.q1{left:90px}.q2{left:379px}.q3{left:660px}
.press .btn-outline{left:902px;top:95px;width:255px;height:54px;border-width:1px;font-size:15px;justify-content:space-between;padding:0 26px}

/* newsletter */
.newsletter{top:2490px;height:150px;background:#121111;border-top:1px solid #2a2a2a}
.nl-title{position:absolute;left:57px;top:30px;font-family:var(--head);font-size:44px;color:var(--pink);text-transform:uppercase}
.nl-text{position:absolute;left:58px;top:83px;width:300px;font-size:15px;line-height:1.6}
.nl-input{position:absolute;left:392px;top:46px;width:330px;height:54px;border:1px solid #555;background:#0c0c0b;display:flex;align-items:center;padding-left:22px;font-size:15px;color:#8c8983}
.newsletter .btn-pink{left:725px;top:46px;width:140px;height:54px}
.social{position:absolute;top:59px;width:30px;height:30px;border-radius:50%;background:var(--pink)}
.s1{left:911px}.s2{left:968px}.s3{left:1025px}.s4{left:1087px}

/* footer */
.site-footer{top:2640px;height:80px;background:#070707;border-top:1px solid #222}
.foot-brand{position:absolute;left:57px;top:17px;font-family:var(--head);font-size:36px;color:var(--yellow);line-height:1}
.foot-sub{position:absolute;left:200px;top:52px;font-family:var(--cond);font-size:8px;letter-spacing:3px}
.foot-nav{position:absolute;left:340px;top:30px;display:flex;gap:30px;font-family:var(--cond);font-weight:600;font-size:14px;text-transform:uppercase}
.copy{position:absolute;right:56px;top:30px;font-family:var(--cond);font-size:15px;color:var(--grey);text-transform:uppercase}
</style>
</head>
<body>
<div class="page">

<section class="hero">
  <div class="hero-photo" role="img" aria-label="Fotografie: Fußballerinnen in Trikots mit Rückennummern, Arm in Arm im Stadionlicht, von hinten"></div>
  <div class="hero-splash"></div>
  <h1 class="hero-title">Sie wollten<br>nur eines:<br><span class="pink">Spielen.</span><br>Sie schrieben<br><span class="yellow">Geschichte.</span></h1>
  <p class="hero-lead">Das neue Musical über Mut, Freundschaft<br>und den Traum von Gleichberechtigung.</p>
  <a class="btn btn-pink" href="#">Jetzt Tickets sichern</a>
  <a class="btn btn-outline" href="#">Trailer ansehen
    <svg width="22" height="22" viewBox="0 0 22 22"><circle cx="11" cy="11" r="9.5" fill="none" stroke="#fff" stroke-width="2"/><path d="M9 7l6 4-6 4z" fill="#fff"/></svg></a>
  <div class="badge"><span class="b1">Weltpremiere</span><span class="b2">Nov 2026</span><span class="b3">Köln</span></div>
</section>

<header class="site-header">
  <div class="brand-kicker">NACH EINER WAHREN GESCHICHTE</div>
  <div class="brand">DANCE PAST DAWN</div>
  <div class="brand-sub">DAS MUSICAL</div>
  <nav class="nav">
    <a href="#">Das Musical</a><a href="#">OURtale</a><a href="#">Cast &amp; Team</a><a href="#">Tickets</a><a href="#">Plan your visit</a><a href="#">Corporate Events</a><a href="#">DE ▾</a>
  </nav>
  <a class="btn btn-pink nav-cta" href="#">Jetzt Tickets sichern</a>
</header>

<section class="ticker">
  <span class="star">★</span><span>Minutenlange Standing Ovations</span>
  <span class="star">★</span><span>Eine wahre Inspiration</span>
  <span class="star">★</span><span>Saal am Lindenhof: ausverkaufte Vorstellungen</span>
  <span class="star">★</span><span>Eine wahre Geschichte</span>
  <span class="star">★</span>
</section>

<section class="story">
  <h2 class="story-title">Vergessen.<br>Verdammt.<br><span class="yellow">Unbesiegbar.</span></h2>
  <p class="story-text">Anfang der 80er Jahre kämpfte die deutsche Frauenfußball-Nationalmannschaft gegen Vorurteile, Benachteiligung und ein ganzes System. Doch sie ließen sich nicht aufhalten.</p>
  <p class="story-claim">DAS IST IHRE GESCHICHTE.</p>
  <a class="btn btn-outline" href="#">Mehr erfahren
    <svg class="arrow" viewBox="0 0 24 12"><path d="M0 6h22M17 1l5 5-5 5" fill="none" stroke="#fff" stroke-width="1.5"/></svg></a>
  <div class="collage">
    <div class="clip clip-1" role="img" aria-label="Schwarzweißfoto: Spielerinnen im Mannschaftskreis"></div>
    <div class="clip clip-2" role="img" aria-label="Vergilbter Zeitungsausschnitt mit abschätziger Schlagzeile über Frauenfußball"></div>
    <div class="clip clip-3" role="img" aria-label="Schwarzweißfoto: jubelndes Team auf dem Platz"></div>
    <div class="clip clip-4" role="img" aria-label="Foto: Protestschild für gleiche Rechte im Sport"></div>
  </div>
</section>

<section class="lead">
  <div class="portrait" role="img" aria-label="Porträt der Hauptfigur Lotte mit lockigem Haar im Trikot"></div>
  <p class="lead-kicker">IM ZENTRUM:</p>
  <h2 class="lead-name">Lotte</h2>
  <p class="lead-text">Talentiert. Ehrgeizig. Unbeirrbar.<br>Lotte will mehr als nur mitspielen.<br>Sie will gewinnen – für sich und für all die, die nicht gehört werden.</p>
  <a class="btn btn-pink" href="#">Lottes Story entdecken
    <svg class="arrow" viewBox="0 0 24 12"><path d="M0 6h22M17 1l5 5-5 5" fill="none" stroke="#fff" stroke-width="1.5"/></svg></a>
</section>

<section class="band">
  <h2 class="band-title">DANCE PAST DAWN</h2>
  <p class="band-sub">EIN MUSICAL, DAS UNTER DIE HAUT GEHT.</p>
  <a class="btn btn-pink" href="#">Mehr über das Musical
    <svg class="arrow" viewBox="0 0 24 12"><path d="M0 6h22M17 1l5 5-5 5" fill="none" stroke="#fff" stroke-width="1.5"/></svg></a>
</section>

<section class="stats">
  <div class="stat">
    <svg viewBox="0 0 82 82" fill="var(--pink)"><circle cx="20" cy="26" r="8"/><circle cx="41" cy="20" r="9"/><circle cx="62" cy="26" r="8"/><path d="M8 70V46q0-8 12-8t12 8v24zM28 72V40q0-9 13-9t13 9v32zM50 70V46q0-8 12-8t12 8v24z"/></svg>
    <div><div class="stat-num">22</div><div class="stat-label">Frauen</div></div>
  </div>
  <div class="stat">
    <svg viewBox="0 0 82 82"><circle cx="41" cy="41" r="36" fill="var(--pink)"/><path d="M41 28l11 8-4 13H34l-4-13z" fill="#0b0b0a"/><path d="M41 5v23M52 36l22-6M48 49l13 18M34 49L21 67M30 36L8 30" stroke="#0b0b0a" stroke-width="3"/></svg>
    <div><div class="stat-num">1</div><div class="stat-label">Traum</div></div>
  </div>
  <div class="stat">
    <svg viewBox="0 0 82 82" fill="var(--pink)"><ellipse cx="41" cy="50" rx="36" ry="16"/><ellipse cx="41" cy="48" rx="24" ry="8" fill="#0b0b0a"/><circle cx="26" cy="24" r="4"/><circle cx="41" cy="20" r="4"/><circle cx="56" cy="24" r="4"/><rect x="22" y="29" width="8" height="9"/><rect x="37" y="25" width="8" height="9"/><rect x="52" y="29" width="8" height="9"/></svg>
    <div><div class="stat-num">1000+</div><div class="stat-label">Hindernisse</div></div>
  </div>
  <div class="stat">
    <svg viewBox="0 0 82 82" fill="var(--pink)"><path d="M22 10h38v20q0 18-19 22-19-4-19-22z"/><path d="M22 16H8q0 20 16 20M60 16h14q0 20-16 20" fill="none" stroke="var(--pink)" stroke-width="4"/><rect x="37" y="52" width="8" height="12"/><rect x="26" y="64" width="30" height="8"/></svg>
    <div><div class="stat-num">1</div><div class="stat-label">Ziel</div></div>
  </div>
</section>

<section class="press">
  <h2 class="press-title">Das sagen die ersten Zuschauer</h2>
  <blockquote class="quote q1"><span class="quote-mark">“</span><p>„Ein Musical, das berührt, wütend macht und Mut schenkt. Ein Muss für alle!“</p><cite>Rheinblatt Tageszeitung</cite></blockquote>
  <blockquote class="quote q2"><span class="quote-mark">“</span><p>„Standing Ovations, Gänsehaut und pure Energie. Weltklasse!“</p><cite>Abendkurier</cite></blockquote>
  <blockquote class="quote q3"><span class="quote-mark">“</span><p>„Diese Geschichte gehört auf die große Bühne. Packend von der ersten bis zur letzten Sekunde.“</p><cite>Westufer Post</cite></blockquote>
  <a class="btn btn-outline" href="#">Weitere Pressestimmen
    <svg class="arrow" viewBox="0 0 24 12"><path d="M0 6h22M17 1l5 5-5 5" fill="none" stroke="#fff" stroke-width="1.5"/></svg></a>
</section>

<section class="newsletter">
  <h2 class="nl-title">Bleib up to date!</h2>
  <p class="nl-text">Erhalte exklusive Updates, Hintergründe und Ticket-Infos direkt in dein Postfach.</p>
  <div class="nl-input">Deine E-Mail-Adresse</div>
  <a class="btn btn-pink" href="#">Anmelden</a>
  <a class="social s1" href="#" aria-label="Social-Media-Kanal 1"></a>
  <a class="social s2" href="#" aria-label="Social-Media-Kanal 2"></a>
  <a class="social s3" href="#" aria-label="Social-Media-Kanal 3"></a>
  <a class="social s4" href="#" aria-label="Social-Media-Kanal 4"></a>
</section>

<footer class="site-footer">
  <div class="foot-brand">DANCE PAST DAWN</div>
  <div class="foot-sub">DAS MUSICAL</div>
  <nav class="foot-nav"><a href="#">FAQ</a><a href="#">Presse</a><a href="#">News</a><a href="#">Impressum</a><a href="#">Datenschutz</a></nav>
  <div class="copy">© 2025 Dosuvel Entertainment GmbH</div>
</footer>

</div>
</body>
</html>
```